Animal Eye Clinic needs a Business card

We are a new veterinary ophthalmology practice (Tessaly Animal Eye Care) and we need a business card designed. We only see animal eyes - we are not a regular veterinary clinic. We already have a logo. We are looking for a professional, good looking business card to hand out to our clients. We are looking for something simple but professional and contemporary. Our logo is likely the only picture/graphic that needs to be on the card.
Updates

Contact Information for Business Card

Marisol Dunkley, BVSc, DVM, PhD, DipECVO
Veterinary Ophthalmologist

Phone: 604.418.3097
Email: tessalyanimaleyecare@mailbrook.net
Website: tessalyanimaleyecare.net
Address: 1840 Pellworth Rd
Larchmere, BC, V4T 8M3

Colors

Designer to choose colors to be used in the design.

Requirements
Must have
• Our logo (attached)

```html
<!DOCTYPE html>
<html lang="en">
<head>
<meta charset="utf-8">
<title>Tessaly Animal Eye Care – Business Card</title>
<link rel="stylesheet" href="https://fonts.googleapis.com/css2?family=Montserrat:wght@400;500;600&display=swap">
<style>
  :root {
    --teal: #0397a8;
    --teal-soft: rgba(255, 255, 255, 0.14);
    --grey: #6b6b6b;
    --white: #ffffff;
    --page: #ffffff;
    --shadow: 0 2px 6px rgba(0, 0, 0, 0.28);
  }
  * { margin: 0; padding: 0; box-sizing: border-box; }
  html, body {
    width: 1200px; height: 1200px; overflow: hidden;
    background: var(--page);
    font-family: "Montserrat", Arial, sans-serif;
  }
  .sheet { position: relative; width: 1200px; height: 1200px; }
  .card { position: absolute; width: 835px; height: 478px; box-shadow: var(--shadow); overflow: hidden; }

  /* Front */
  .card-front { left: 185px; top: 82px; background: var(--teal); }
  .front-decor {
    position: absolute; left: 560px; top: 40px; width: 380px; height: 380px;
    border-radius: 50%; background: var(--teal-soft);
  }
  .front-mark {
    position: absolute; left: 150px; top: 195px; width: 90px; height: 90px;
    border-radius: 50%; background: var(--white);
  }
  .front-name {
    position: absolute; left: 270px; top: 222px;
    color: var(--white); font-size: 30px; font-weight: 600; line-height: 36px;
    white-space: nowrap;
  }

  /* Back */
  .card-back { left: 187px; top: 625px; background: var(--white); }
  .back-mark {
    position: absolute; left: 75px; top: 110px; width: 250px; height: 250px;
    border-radius: 50%; background: var(--teal);
  }
  .divider {
    position: absolute; left: 402px; top: 81px; width: 2px; height: 316px; background: var(--teal);
  }
  .details { position: absolute; left: 415px; top: 75px; color: var(--grey); }
  .person-name { color: var(--teal); font-size: 33px; font-weight: 500; letter-spacing: 0.5px; line-height: 1.1; }
  .credentials, .role { font-size: 18.5px; line-height: 26px; }
  .practice-name { color: var(--teal); font-size: 19px; font-weight: 500; letter-spacing: 0.5px; margin-top: 32px; }
  .address { font-size: 19px; line-height: 30px; margin-top: 6px; }
  .contact-list { list-style: none; margin-top: 24px; }
  .contact-list li { display: flex; align-items: center; font-size: 18px; line-height: 30px; }
  .contact-list svg { width: 20px; height: 20px; margin-right: 11px; fill: var(--teal); flex: none; }
</style>
</head>
<body>
<main class="sheet">
  <section class="card card-front" aria-label="Card front">
    <div class="front-decor" role="img" aria-label="Faint background area for the practice mark"></div>
    <div class="front-mark" aria-hidden="true"></div>
    <h1 class="front-name">Tessaly Animal Eye Care</h1>
  </section>

  <section class="card card-back" aria-label="Card back">
    <div class="back-mark" role="img" aria-label="Practice mark area"></div>
    <div class="divider"></div>
    <div class="details">
      <h2 class="person-name">MARISOL DUNKLEY</h2>
      <p class="credentials">BVSc, DVM, PhD, DipECVO</p>
      <p class="role">Veterinary Ophthalmologist</p>
      <p class="practice-name">TESSALY ANIMAL EYE CARE</p>
      <p class="address">1840 Pellworth Rd<br>Larchmere, BC, V4T 8M3</p>
      <ul class="contact-list">
        <li>
          <svg viewBox="0 0 24 24" aria-hidden="true"><path d="M6.6 10.8a15.2 15.2 0 0 0 6.6 6.6l2.2-2.2a1 1 0 0 1 1-.25 11.4 11.4 0 0 0 3.6.57 1 1 0 0 1 1 1V20a1 1 0 0 1-1 1A17 17 0 0 1 3 4a1 1 0 0 1 1-1h3.5a1 1 0 0 1 1 1c0 1.25.2 2.45.57 3.57a1 1 0 0 1-.25 1z"/></svg>
          604.418.3097
        </li>
        <li>
          <svg viewBox="0 0 24 24" aria-hidden="true"><path d="M2 5h20v14H2z M4 7v.4l8 5.6 8-5.6V7l-8 5.6z" fill-rule="evenodd"/></svg>
          tessalyanimaleyecare@mailbrook.net
        </li>
        <li>
          <svg viewBox="0 0 24 24" aria-hidden="true"><circle cx="12" cy="12" r="10"/><path d="M2 12h20M12 2c3 3 3 17 0 20M12 2c-3 3-3 17 0 20" stroke="#fff" stroke-width="1.4" fill="none"/></svg>
          www.tessalyanimaleyecare.net
        </li>
      </ul>
    </div>
  </section>
</main>
</body>
</html>
```